Evening on Willow Quay

I need a jpeg of a poster advertising a church party
It has a jazzy, fun theme. Details

An Evening on Willow Quay
Friday, June 14th from 8-11 PM
Party for all Ridgeline Parish adults at the Stake Centre
Fun, food, friends,live music, a chance to mingle and relax!
A great chance to bring your friends for a fun evening!

Id like some sort of jazz picture or shadowy picture....not really sure but I need it super fast so that I can have it printed Saturday...can anyone help me? I want it to be fun and snappy looking without being racy...no naked women :)

• naked or half dressed women, cigarettes, alcohol

```html
<!DOCTYPE html>
<html lang="en">
<head>
<meta charset="utf-8">
<title>An Evening on Willow Quay</title>
<link rel="stylesheet" href="https://fonts.googleapis.com/css2?family=Archivo+Narrow:wght@700&family=Metamorphous&display=swap">
<style>
  :root {
    --ink: #121416;
    --swoosh: #9fc2d8;
    --sky: #6db8e6;
    --title-top: #5bb6ea;
    --title-mid: #ffffff;
    --title-band: #3d8fe0;
    --title-low: #4a3b9a;
    --white: #ffffff;
  }
  * { margin: 0; padding: 0; box-sizing: border-box; }
  html, body { width: 934px; height: 1200px; overflow: hidden; background: var(--ink); }
  .poster {
    position: relative;
    width: 934px;
    height: 1200px;
    overflow: hidden;
    background: var(--ink);
    font-family: "Metamorphous", serif;
    color: var(--white);
  }
  .poster-backdrop { position: absolute; inset: 0; width: 934px; height: 1200px; }
  .poster-text { position: absolute; white-space: nowrap; font-variant: small-caps; }
  .kicker {
    right: 72px; top: 105px;
    font-size: 58px; letter-spacing: 2px; text-transform: lowercase;
  }
  .kicker::first-letter { text-transform: uppercase; }
  .event-title {
    position: absolute; left: 50px; top: 168px; width: 834px;
    font-family: "Archivo Narrow", "Arial Narrow", Arial, sans-serif;
    font-weight: 700; font-size: 146px; line-height: 1; letter-spacing: -2px;
    white-space: nowrap; text-align: center;
    background: linear-gradient(180deg,
      var(--title-top) 12%, var(--title-mid) 48%, var(--title-mid) 64%,
      var(--title-band) 66%, #8fc8f2 70%, var(--title-low) 92%);
    -webkit-background-clip: text; background-clip: text;
    color: transparent;
  }
  .event-date {
    left: 80px; top: 392px;
    font-size: 42px; color: var(--sky);
  }
  .event-time { left: 78px; top: 465px; font-size: 40px; }
  .event-time .hours {
    font-family: "Archivo Narrow", "Arial Narrow", Arial, sans-serif;
    font-variant: normal; font-weight: 700; font-size: 58px; margin-left: 12px;
  }
  .event-details {
    position: absolute; right: 38px; top: 625px; text-align: right;
    font-size: 44px; line-height: 79px; color: var(--sky); font-variant: small-caps;
    white-space: nowrap;
  }
  .invite {
    position: absolute; left: 32px; top: 1025px;
    font-size: 38px; line-height: 68px; font-variant: small-caps;
    white-space: nowrap;
  }
  .invite span { display: block; }
  .invite .second { padding-left: 19px; }
</style>
</head>
<body>
<main class="poster">
  <svg class="poster-backdrop" viewBox="0 0 934 1200" aria-hidden="true">
    <defs>
      <radialGradient id="haze-glow" cx="0.55" cy="0.55" r="0.65">
        <stop offset="0" stop-color="#7b8084"/>
        <stop offset="0.6" stop-color="#4b4f53"/>
        <stop offset="1" stop-color="#1c1e21"/>
      </radialGradient>
      <linearGradient id="streak-fade" x1="0" x2="1">
        <stop offset="0" stop-color="#d9423a" stop-opacity="0"/>
        <stop offset="0.35" stop-color="#d9423a" stop-opacity="0.8"/>
        <stop offset="1" stop-color="#d9423a"/>
      </linearGradient>
      <linearGradient id="streak-fade-back" x1="0" x2="1">
        <stop offset="0" stop-color="#d9423a" stop-opacity="0.1"/>
        <stop offset="1" stop-color="#d9423a"/>
      </linearGradient>
      <linearGradient id="floor-band" x1="0" y1="0" x2="0" y2="1">
        <stop offset="0" stop-color="#1d2a33"/>
        <stop offset="1" stop-color="#121416"/>
      </linearGradient>
    </defs>
    <rect width="934" height="1200" fill="var(--ink)"/>
    <path d="M0 0 H934 V540 Q560 710 0 600 Z" fill="url(#haze-glow)"/>
    <rect x="380" y="965" width="554" height="235" fill="url(#floor-band)"/>
    <g fill="var(--swoosh)">
      <path d="M0 70 Q520 -40 560 330 L560 1200 L500 1200 L500 360 Q470 40 0 150 Z" opacity="0.35"/>
      <path d="M0 0 Q620 -30 660 320 Q700 820 934 930 L934 990 Q640 860 600 340 Q560 40 0 40 Z" opacity="0.28"/>
      <path d="M0 210 Q400 180 440 420 L440 1200 L380 1200 L380 440 Q360 250 0 280 Z" opacity="0.22"/>
      <path d="M934 540 Q780 900 560 1200 L620 1200 Q840 900 934 620 Z" opacity="0.25"/>
      <path d="M710 0 Q860 250 934 300 L934 250 Q860 200 770 0 Z" opacity="0.15"/>
    </g>
    <polygon points="140,320 910,336 140,345" fill="url(#streak-fade)"/>
    <polygon points="400,1110 934,1118 400,1126" fill="url(#streak-fade-back)"/>
    <line x1="18" y1="419" x2="82" y2="419" stroke="var(--sky)" stroke-width="2"/>
  </svg>

  <p class="poster-text kicker">An Evening on</p>
  <h1 class="event-title">Willow Quay</h1>

  <p class="poster-text event-date">Friday, June 14th</p>
  <p class="poster-text event-time">From <span class="hours">8 - 11 PM</span></p>

  <p class="event-details">
    party for All<br>
    Ridgeline Parish Adults<br>
    At the Stake centre
  </p>

  <p class="invite">
    <span>A great chance to Bring your friends</span>
    <span class="second">for A fun evening!</span>
  </p>
</main>
</body>
</html>
```